Psychology service brochure

Marketing brochure for a new psychological counselling service.
Our old brochure was too boring and conservative. We are selling our services to GP's, psychiatrists, other health providers and of course potential clients. We'd really like a professional, elegant look that conveys us to be compassionate and conscientious providers of psychological services.
I have included a copy of our old brochure and a copy of the changes we'd like to the text.
Updates
I have included a photo of myself and my business partner. Only the faces are needed, so backgrounds would need to be edited out.
Hello, in consultation with my business partner, we would like
the use of our photos in the brochure please (with backgrounds edited out)
no stock photos of random people
use of abstract or nature/floral motifs suggestive of tranquillity
regards,
Miriam
Target Market(s)
General practitioner doctors, potential clients
Industry/Entity Type
Health
Requirements
Must have
- must include BlairMdITC TT- font for the business name
- must include our signature color Pantone 291 (see attached brochure)
- use of the photos of myself and my business partner (with background edited out please)
- keep use of colours to a minimum, 3 colors maximum, one of which must be Pantone 291
- must include changes to the brochure as outlined in the 'Changes to Pamphlet' document.
Nice to have
- an interesting, eye catching layout.
- interesting use of white spaces
- use of subtle abstract or nature/floral related graphics suggestive of tranquillity
Should not have
- should not include our fee
- stock photos of people

```html
<!DOCTYPE html>
<html lang="en">
<head>
<meta charset="utf-8">
<title>Quiet Harbour Counselling – Brochure</title>
<link rel="stylesheet" href="https://fonts.googleapis.com/css2?family=Marcellus+SC&family=Questrial&display=swap">
<style>
  :root {
    --paper: #ffffff;
    --ink-dark: #1c1d1f;
    --brand-blue: #a4d9f4;
    --text-blue: #3bb6e8;
    --heading-white: #f2f4f5;
    --trim: #9a9a9a;
    --photo-shadow: #141414;
    --photo-skin: #c9b6a6;
    --photo-hair: #d9c9a8;
  }
  * { margin: 0; padding: 0; box-sizing: border-box; }
  html, body { width: 1200px; height: 900px; overflow: hidden; background: var(--paper); }
  .spread {
    position: relative; width: 1200px; height: 900px;
    font-family: "Questrial", sans-serif; color: var(--text-blue);
  }
  .trim-marks { position: absolute; inset: 0; }
  .sheet {
    position: absolute; left: 20px; top: 30px; width: 1160px; height: 835px;
    background: var(--ink-dark);
  }
  .portrait {
    position: absolute; left: 783px; top: 30px; width: 397px; height: 835px;
    background:
      radial-gradient(ellipse 55% 30% at 75% 18%, var(--photo-hair) 0%, rgba(217,201,168,0) 100%),
      radial-gradient(ellipse 50% 40% at 55% 48%, var(--photo-skin) 0%, rgba(201,182,166,0) 100%),
      radial-gradient(ellipse 45% 25% at 80% 78%, #b8a596 0%, rgba(184,165,150,0) 100%),
      var(--photo-shadow);
  }
  .brand-vertical {
    position: absolute; left: 1108px; top: 732px;
    transform: rotate(-90deg); transform-origin: 0 0;
    font-family: "Marcellus SC", serif; font-size: 33px; letter-spacing: 6px;
    color: var(--brand-blue); white-space: nowrap; line-height: 32px;
  }

  .column-about { position: absolute; left: 83px; top: 155px; width: 290px; }
  .section-title {
    font-size: 19px; line-height: 22px; color: var(--heading-white); font-weight: 400;
    white-space: nowrap; margin-bottom: 19px;
  }
  .section-title.second { margin-top: 31px; margin-bottom: 19px; }
  .body-copy { font-size: 14px; line-height: 18.8px; margin-bottom: 18.8px; }
  .body-copy .line {
    display: block; white-space: nowrap;
    text-align: justify; text-align-last: justify;
  }
  .body-copy .line.last { text-align-last: left; }

  .goals { list-style: none; font-size: 14px; line-height: 18.8px; }
  .goals li { position: relative; padding-left: 15px; white-space: nowrap; }
  .goals li::before { content: "•"; position: absolute; left: 0; top: 0; font-size: 11px; }

  .location-map {
    position: absolute; left: 428px; top: 168px; width: 338px; height: 283px;
    background:
      radial-gradient(ellipse 60% 55% at 50% 50%, rgba(164,217,244,0.35) 0%, rgba(164,217,244,0.08) 100%),
      var(--ink-dark);
    border: 1px solid rgba(164,217,244,0.4);
  }

  .contact {
    position: absolute; left: 430px; top: 522px; width: 340px; text-align: center;
    font-style: normal; font-size: 14px; line-height: 20px;
  }
  .contact .centre-name { font-size: 19px; line-height: 26px; margin: 0 0 2px; }
  .contact .address { margin-bottom: 30px; }
  .contact .lines div { line-height: 22px; }

  .banner {
    position: absolute; left: 13px; top: 752px; width: 1169px; height: 56px;
    background: var(--brand-blue);
  }
  .banner-name {
    position: absolute; top: 19px;
    font-family: "Marcellus SC", serif; font-size: 17px; letter-spacing: 2.6px;
    color: var(--text-blue); white-space: nowrap; line-height: 1;
  }
</style>
</head>
<body>
<div class="spread">
  <svg class="trim-marks" width="1200" height="900" aria-hidden="true">
    <g stroke="var(--trim)" stroke-width="0.8">
      <line x1="33" y1="0" x2="33" y2="18"/><line x1="1164" y1="0" x2="1164" y2="18"/>
      <line x1="33" y1="882" x2="33" y2="900"/><line x1="1164" y1="882" x2="1164" y2="900"/>
      <line x1="0" y1="46" x2="14" y2="46"/><line x1="1186" y1="46" x2="1200" y2="46"/>
      <line x1="0" y1="851" x2="14" y2="851"/><line x1="1186" y1="851" x2="1200" y2="851"/>
    </g>
  </svg>

  <div class="sheet"></div>
  <div class="portrait" role="img" aria-label="Portrait photograph of a woman with swept blonde hair against a dark background"></div>
  <div class="brand-vertical">Quiet Harbour Counselling</div>

  <section class="column-about">
    <h2 class="section-title">Our Approach to Therapy</h2>
    <p class="body-copy">
      <span class="line">We are warm, compassionate and profes-</span>
      <span class="line">sional Clinical and General Psychologists</span>
      <span class="line">who together have thirty years of experi-</span>
      <span class="line">ence and who are committed to providing</span>
      <span class="line">high quality evidence-based treatment to</span>
      <span class="line last">our clients.</span>
    </p>
    <p class="body-copy">
      <span class="line">Types of treatment may include Cognitive</span>
      <span class="line">Behavioural Therapy, Motivational Inter-</span>
      <span class="line">viewing and Mindfulness. Eligible to provide</span>
      <span class="line">Pregnancy Support Counselling services</span>
      <span class="line last">under Medicare</span>
    </p>
    <h2 class="section-title second">What We Want For Our Clients</h2>
    <ul class="goals">
      <li>For you to feel heard and respected.</li>
      <li>To have a positive experience of<br>working collaboratively with a<br>psychologist.</li>
      <li>To connect or reconnect with<br>feelings of hope.</li>
      <li>To move beyond counseling with<br>an understanding of your own<br>strengths and the skills to make<br>changes that will help you meet<br>future challenges.</li>
    </ul>
  </section>

  <div class="location-map" role="img" aria-label="Street map in light blue lines showing the centre's location beside the train station"></div>

  <address class="contact">
    <div>Contact reception</div>
    <div class="centre-name">The Wexford Centre</div>
    <div class="address">17 Wexford Street, Ashvale 3071</div>
    <div class="lines">
      <div>Phone: 9410 2736</div>
      <div>Fax: 9410 2737</div>
      <div>Email: qhcounsel@mailbox.com</div>
    </div>
  </address>

  <div class="banner">
    <span class="banner-name" style="left:43px">Quiet Harbour Counselling</span>
    <span class="banner-name" style="left:416px">Quiet Harbour Counselling</span>
    <span class="banner-name" style="left:796px">Quiet Harbour Counselling</span>
  </div>
</div>
</body>
</html>
```